Business cards for Tile Contractor
Brisk Grout Studio
LAST MINUTE ADDITION TO BUSINESS CARD!!
website address: briskgroutstudio.net
and a space after the area code in phone number:
thanks!!
#85 is closest to what im looking for. Thanks for all the drafts! good stuff!
looks good so far. would like to see more with all the info on the card.

```html
<!DOCTYPE html>
<html lang="en">
<head>
<meta charset="utf-8">
<title>Brisk Grout Studio – Stationery</title>
<link href="https://fonts.googleapis.com/css2?family=Exo+2:wght@700&family=Open+Sans:ital,wght@0,400;0,600;1,400&display=swap" rel="stylesheet">
<style>
  :root {
    --navy: #0f1d33;
    --deep: #14345e;
    --blue: #1f6fc2;
    --bright: #3fa3ea;
    --ink: #1d2f4f;
    --grey: #6b7280;
    --paper: #ffffff;
    --stage: #e8eaee;
  }
  * { box-sizing: border-box; margin: 0; padding: 0; }
  html, body { width: 1200px; height: 778px; overflow: hidden; }
  body { background: var(--stage); font-family: "Open Sans", Arial, sans-serif; color: var(--ink); position: relative; }

  .sheet { position: absolute; background: var(--paper); box-shadow: 0 3px 12px rgba(0,0,0,.15); overflow: hidden; }
  .brand { display: flex; align-items: center; gap: 8px; }
  .brand-mark { width: 20px; height: 20px; background: var(--ink); flex: none; }
  .brand-name { font-family: "Exo 2", Arial, sans-serif; font-weight: 700; font-size: 17px; color: var(--ink); letter-spacing: .5px; text-transform: uppercase; white-space: nowrap; }
  .brand.light .brand-mark { background: #fff; }
  .brand.light .brand-name { color: #fff; }

  .swoosh { position: absolute; left: 0; bottom: 0; width: 100%; display: block; }
  .band-text { position: absolute; left: 20px; bottom: 10px; color: #fff; font-size: 9px; font-weight: 600; }

  /* Letterhead */
  .letterhead { left: 45px; top: 85px; width: 470px; height: 608px; }
  .letterhead .brand { position: absolute; left: 26px; top: 30px; }
  .contact-block { position: absolute; left: 300px; top: 28px; font-size: 7px; line-height: 11px; color: var(--grey); padding-left: 8px; border-left: 1px solid #cfd4db; }
  .faint-disc { position: absolute; left: 80px; top: 180px; width: 300px; height: 300px; border-radius: 50%; background: #f3f4f6; }

  /* Envelope */
  .envelope { left: 565px; top: 50px; width: 600px; height: 262px; }
  .envelope .flap { position: absolute; left: 0; top: 0; width: 100%; }
  .envelope .flap-brand { position: absolute; left: 50%; top: 16px; transform: translateX(-50%); }
  .envelope .return-brand { position: absolute; left: 24px; top: 92px; }
  .return-address { position: absolute; left: 24px; top: 172px; font-size: 8px; line-height: 12px; color: var(--grey); }
  .window { position: absolute; right: 40px; top: 96px; width: 190px; height: 56px; border: 1px solid #c7ccd3; border-radius: 6px; background: #eef0f3; }

  /* Cards */
  .card { width: 290px; height: 166px; border-radius: 4px; }
  .card-front { left: 565px; top: 345px; }
  .card-back { left: 875px; top: 345px; background: linear-gradient(160deg, var(--blue), var(--deep) 55%, var(--navy)); }
  .card-contact { left: 720px; top: 545px; }
  .card .center-brand { position: absolute; left: 50%; top: 34px; transform: translateX(-50%); }
  .tagline { position: absolute; left: 0; width: 100%; top: 82px; text-align: center; font-size: 9px; font-style: italic; color: var(--ink); }
  .tagline small { display: block; font-style: normal; font-size: 7px; color: var(--grey); margin-top: 3px; }
  .card-back .tagline, .card-back .tagline small { color: #e6f1fb; }
  .card-contact .brand { position: absolute; left: 16px; top: 20px; }
  .person { position: absolute; right: 16px; top: 56px; text-align: right; }
  .person-name { font-size: 10px; font-weight: 600; letter-spacing: 1px; color: var(--ink); }
  .person-role { font-size: 7px; color: var(--grey); }
  .card-details { position: absolute; left: 16px; top: 66px; font-size: 7px; line-height: 11px; color: var(--grey); }
</style>
</head>
<body>

<section class="sheet letterhead" aria-label="Letterhead">
  <div class="brand"><span class="brand-mark"></span><span class="brand-name">Brisk Grout Studio</span></div>
  <address class="contact-block">418 Harbor Lane<br>Coastview, CA 90000<br>(805) 555 0148<br>info@briskgroutstudio.net</address>
  <div class="faint-disc"></div>
  <svg class="swoosh" viewBox="0 0 470 60" height="60" preserveAspectRatio="none">
    <defs><linearGradient id="lhBand" x1="0" x2="1"><stop offset="0" stop-color="#0f1d33"/><stop offset=".6" stop-color="#14345e"/><stop offset="1" stop-color="#1f6fc2"/></linearGradient></defs>
    <path d="M0 28 Q235 18 470 6 L470 60 L0 60 Z" fill="#3fa3ea"/>
    <path d="M0 32 Q235 24 470 12 L470 60 L0 60 Z" fill="url(#lhBand)"/>
  </svg>
  <span class="band-text">www.briskgroutstudio.net</span>
</section>

<section class="sheet envelope" aria-label="Envelope">
  <svg class="flap" viewBox="0 0 600 72" height="72" preserveAspectRatio="none">
    <defs><linearGradient id="flapGrad" x1="0" x2="1"><stop offset="0" stop-color="#0f1d33"/><stop offset=".5" stop-color="#1f6fc2"/><stop offset="1" stop-color="#0f1d33"/></linearGradient></defs>
    <path d="M0 0 H600 V58 Q300 78 0 58 Z" fill="url(#flapGrad)"/>
    <path d="M0 58 Q300 78 600 58" stroke="#3fa3ea" stroke-width="2" fill="none"/>
  </svg>
  <div class="brand light flap-brand"><span class="brand-mark"></span><span class="brand-name">Brisk Grout Studio</span></div>
  <div class="brand return-brand"><span class="brand-mark"></span><span class="brand-name">Brisk Grout Studio</span></div>
  <address class="return-address">418 Harbor Lane<br>Coastview, CA 90000</address>
  <div class="window"></div>
  <svg class="swoosh" viewBox="0 0 600 40" height="40" preserveAspectRatio="none">
    <defs><linearGradient id="envBand" x1="0" x2="1"><stop offset="0" stop-color="#0f1d33"/><stop offset=".7" stop-color="#14345e"/><stop offset="1" stop-color="#1f6fc2"/></linearGradient></defs>
    <path d="M0 14 Q300 10 600 2 L600 40 L0 40 Z" fill="#3fa3ea"/>
    <path d="M0 18 Q300 14 600 7 L600 40 L0 40 Z" fill="url(#envBand)"/>
  </svg>
  <span class="band-text">www.briskgroutstudio.net</span>
</section>

<section class="sheet card card-front" aria-label="Business card front">
  <div class="brand center-brand"><span class="brand-mark"></span><span class="brand-name">Brisk Grout Studio</span></div>
  <p class="tagline">" Quality tile installation at an affordable price "<small>Residential &amp; Commercial • Free Estimates</small></p>
  <svg class="swoosh" viewBox="0 0 290 26" height="26" preserveAspectRatio="none">
    <path d="M0 10 Q145 6 290 0 L290 26 L0 26 Z" fill="#3fa3ea"/>
    <path d="M0 13 Q145 9 290 4 L290 26 L0 26 Z" fill="#14345e"/>
  </svg>
</section>

<section class="sheet card card-back" aria-label="Business card back">
  <div class="brand light center-brand"><span class="brand-mark"></span><span class="brand-name">Brisk Grout Studio</span></div>
  <p class="tagline">" Quality tile installation at an affordable price "<small>Residential &amp; Commercial • Free Estimates</small></p>
</section>

<section class="sheet card card-contact" aria-label="Business card with contact details">
  <div class="brand"><span class="brand-mark"></span><span class="brand-name">Brisk Grout Studio</span></div>
  <div class="person"><div class="person-name">ZANDU MARSH</div><div class="person-role">Owner</div></div>
  <address class="card-details">418 Harbor Lane<br>Coastview, CA 90000<br>Cell (805) 555 0199<br>info@briskgroutstudio.net<br>briskgroutstudio.net</address>
  <svg class="swoosh" viewBox="0 0 290 22" height="22" preserveAspectRatio="none">
    <path d="M0 8 Q145 5 290 0 L290 22 L0 22 Z" fill="#3fa3ea"/>
    <path d="M0 11 Q145 8 290 4 L290 22 L0 22 Z" fill="#14345e"/>
  </svg>
</section>

</body>
</html>
```